Business Card Design Project

use presentation folder design and my logo and make 4 over 4 business cards

Industry/Entity Type

Business

Requirements
Must have
• use the design from my presentation folder and put my logo on it

Name
Title
phone
fax
email

```html
<!DOCTYPE html>
<html lang="en">
<head>
<meta charset="utf-8">
<title>Kindpath – Business Card</title>
<link href="https://fonts.googleapis.com/css2?family=Lato:wght@400;700&family=Merriweather:wght@700&display=swap" rel="stylesheet">
<style>
  :root{
    --page:#e9e6e2;
    --card-front:#ede1d9;
    --wash-from:#e6d6cb;
    --wash-to:#ede1d9;
    --ink:#2f2a27;
    --brown:#8a562a;
    --brown-tile:#6f4323;
    --charcoal:#3d3d3d;
    --stone:#d7d2c4;
    --blush:#e6ddd9;
    --mist:#dcdde0;
    --gap:#f7f5f3;
    --logo-grey:#6e6a67;
  }
  *{box-sizing:border-box;margin:0;padding:0}
  html,body{width:1200px;height:1023px;overflow:hidden}
  body{background:var(--page);position:relative;font-family:'Lato',sans-serif;color:var(--ink)}
  .card{position:absolute;left:222px;width:756px;height:432px;border-radius:6px;overflow:hidden;box-shadow:0 4px 14px rgba(0,0,0,.15)}
  .card--front{top:53px;background:var(--card-front)}
  .card--back{top:538px;background:var(--gap)}
  .card__wash{position:absolute;left:0;top:0;width:360px;height:432px;background:linear-gradient(160deg,var(--wash-to) 0%,var(--wash-from) 100%)}
  .tab{position:absolute;background:var(--charcoal);border-radius:6px}
  .card--front .tab{right:-8px;top:26px;width:22px;height:70px}
  .wordmark{position:absolute;display:flex;align-items:center;gap:10px;font-family:'Lato',sans-serif;font-weight:700;color:var(--logo-grey)}
  .wordmark__dot{width:18px;height:18px;border-radius:50%;background:var(--logo-grey)}
  .card--front .wordmark{left:80px;top:292px;font-size:34px}
  .contact{position:absolute;left:372px;top:92px}
  .contact__name{font-size:31px;font-weight:700;color:var(--brown);line-height:1.1}
  .contact__title{font-family:'Merriweather',serif;font-size:16px;font-weight:700;margin-top:4px}
  .contact__address{font-size:20px;line-height:1.4;margin-top:22px}
  .contact__lines{list-style:none;margin-top:18px;font-size:19px;line-height:1.35}
  .contact__lines li{display:flex;align-items:center;gap:12px}
  .contact__lines svg{width:14px;height:14px;fill:var(--brown)}
  .tile{position:absolute;border-radius:16px}
  .tile--blush{left:14px;top:-16px;width:210px;height:88px;background:var(--blush)}
  .tile--stone{left:14px;top:86px;width:210px;height:150px;background:var(--stone)}
  .tile--mist{left:238px;top:-16px;width:534px;height:252px;background:var(--mist)}
  .tile--charcoal{left:-16px;top:250px;width:240px;height:200px;background:var(--charcoal)}
  .tile--brown{left:238px;top:250px;width:430px;height:200px;background:var(--brown-tile)}
  .tile--edge{left:682px;top:250px;width:90px;height:200px;background:var(--charcoal)}
  .card--back .wordmark{left:380px;top:96px;font-size:36px}
  .web{position:absolute;left:270px;top:388px;font-size:22px;color:#fff;letter-spacing:.5px}
  .card--back .tab{left:-8px;top:300px;width:22px;height:56px;background:var(--stone)}
</style>
</head>
<body>
  <section class="card card--front" aria-label="Card front">
    <div class="card__wash" role="img" aria-label="Soft decorative background area behind the company name"></div>
    <div class="tab"></div>
    <div class="wordmark"><span class="wordmark__dot"></span>Kindpath</div>
    <div class="contact">
      <p class="contact__name">Marcus Hale</p>
      <p class="contact__title">Managing Director</p>
      <p class="contact__address">120 Elmwood Dr, Suite 4<br>Fairview, VA 22010</p>
      <ul class="contact__lines">
        <li><svg viewBox="0 0 14 14"><path d="M3 1l3 3-2 2c1 2 2 3 4 4l2-2 3 3-2 2C6 13 1 8 1 3z"/></svg>555-018-2234</li>
        <li><svg viewBox="0 0 14 14"><rect x="1" y="5" width="12" height="8" rx="1"/><rect x="4" y="1" width="6" height="4"/></svg>555-018-3412</li>
        <li><svg viewBox="0 0 14 14"><path d="M1 3h12v9H1z M1 3l6 5 6-5"/></svg>info@kindpath.com</li>
      </ul>
    </div>
  </section>

  <section class="card card--back" aria-label="Card back">
    <div class="tile tile--blush"></div>
    <div class="tile tile--stone"></div>
    <div class="tile tile--mist"></div>
    <div class="tile tile--charcoal"></div>
    <div class="tile tile--brown"></div>
    <div class="tile tile--edge"></div>
    <div class="wordmark"><span class="wordmark__dot"></span>Kindpath</div>
    <p class="web">www.kindpath.com</p>
    <div class="tab"></div>
  </section>
</body>
</html>
```